WebDesign | Financial Services Firm - Risk Mitigation

We are a professional services consulting firm that specializes in high net worth individuals over $25,000,000, executives C-suite and above, closely held businesses owners, family offices and highly compensated employees.

Our focus is on risk mitigation and tax efficient strategies. Our clients take their risk on themselves and have a proven track record generating wealth. Our directive is to preserve and protect the wealth they’ve already created.

Our company Harbor Crest Advisory is geared around five directives of asset protection:
1) Legal Structuring
2) Leverage & Financing
3) Risk Management - Asset Protection & Insurance, Trustee Work
4) Asset Management & Investing - Under www.tqlvalemark.com
5) Tax Efficient Strategies

Our Company Mark is a Pentagon with a key in the middle. A pentagon is the most efficient defensive structure. Each point of a pentagon is equal distance front every point . Each side provides support to another and works together, which is the key to our clients success.

Our key colors are blue, black and silver.

We ‘re located in the Pacific Northwest with bi coastal and international clients. We have fewer, higher net worth clients and provide exceptional customer service. We do not do social media.

We'll need the following pages:
-Front Landing Page.
Front page has to have link to hbportal.docuvaultix.com for logging into secure site.
- Contact & About Us Page
- Our Team Page
- Five Sides of Wealth Management
> Legal & Business Structuring
> Leverage & Financing
> Risk Management & Asset Protection.
> Asset Management and Investing - Will link to TQL (won't be turned on for a few months)
> Tax Efficient Strategies.

Industry/Entity Type

Financial Service

Coding

Coded - Design and coding required

Number of Pages Required

5+ page

Font styles to use
Sans Serif

Colors
0555a3

Requirements
Must have
• Our key colors are blue, black and silver.

-Front Landing Page.
- Contact & About Us Page
- Our Team Page
> Leverage & Financing
Nice to have
• I have attached images that have been purchased for use on the webpage. Us or not.

location page: 847 W Alder Ln, Suite 412, Lake Oswego, OR 97035
Should not have
• lots of color.

```html
<!DOCTYPE html>
<html lang="en">
<head>
<meta charset="utf-8">
<title>Harbor Crest Advisory — Financial Services Firm</title>
<link rel="stylesheet" href="https://fonts.googleapis.com/css2?family=Poppins:wght@600;700;800&family=IBM+Plex+Sans:wght@400;500;600&display=swap">
<style>
:root{
  --blue:#0b45a0;
  --blue-deep:#0a3a8c;
  --navy:#0d1d5c;
  --ink:#111827;
  --text:#2b2b2b;
  --grey-bg:#f4f1f3;
  --footer:#1b1b1b;
  --footer-text:#d9d9d9;
  --white:#ffffff;
  --line:#d8d8d8;
}
*{box-sizing:border-box;margin:0;padding:0}
html,body{width:1200px;height:3085px;overflow:hidden}
body{position:relative;font-family:"IBM Plex Sans",Arial,sans-serif;color:var(--text);background:var(--white)}
a{text-decoration:none}
.abs{position:absolute}
.heading{font-family:"Poppins",Arial,sans-serif;font-weight:800;letter-spacing:-.5px;color:var(--ink)}
.divider{position:absolute;left:50%;transform:translateX(-50%);width:114px;height:3px;display:flex;justify-content:space-between}
.divider span{width:50px;height:2px;background:linear-gradient(90deg,#fff,var(--blue),#fff)}
.btn{display:inline-block;font-family:"IBM Plex Sans",sans-serif;font-weight:500}

/* hero */
.hero{left:0;top:0;width:1200px;height:635px;background:linear-gradient(180deg,#b9cce6 0%,#c8d3e4 22%,#a9a6b5 45%,#7a5a45 70%,#4a3326 100%)}
.logo{left:132px;top:32px;display:flex;align-items:center;gap:12px}
.logo-square{width:40px;height:40px;background:var(--navy)}
.logo-name{font-family:"IBM Plex Sans",sans-serif;font-weight:600;font-size:22px;color:var(--navy);letter-spacing:.5px}
.nav{right:132px;top:31px;display:flex;gap:34px;font-size:15px;font-weight:500}
.nav a{color:#111}
.nav a.active{color:var(--blue);text-decoration:underline;text-underline-offset:4px;font-weight:600}
.hero-title{left:0;width:1200px;top:108px;text-align:center;font-size:30px;color:var(--navy)}
.hero-sub{left:0;width:1200px;top:155px;text-align:center;font-size:18px;color:#1a1a1a}
.hero-btn{left:545px;top:192px;width:110px;height:32px;line-height:32px;text-align:center;background:var(--blue);color:#fff;font-size:15px}
.dots{left:561px;top:589px;display:flex;gap:8px;align-items:center}
.dots i{display:block;width:7px;height:7px;border-radius:50%;background:#fff}
.dots i.on{width:11px;height:11px;border:2px solid #fff;background:var(--blue)}

/* five sides */
.five-title{left:0;width:1200px;top:674px;text-align:center;font-size:22px}
.pillar h3{font-family:"Poppins",sans-serif;font-weight:700;font-size:16px;color:var(--navy);margin-bottom:6px;white-space:nowrap}
.pillar p{font-size:12.5px;line-height:16px;color:#222}
.pillar.right{text-align:right}
.pillar.center{text-align:center}
.icon-ring{width:76px;height:76px;border:2px solid var(--navy);border-radius:50%;display:flex;align-items:center;justify-content:center}
.hub{left:520px;top:960px;width:176px;height:170px;display:flex;flex-direction:column;align-items:center;justify-content:center;gap:14px}
.hub-square{width:80px;height:80px;background:var(--navy)}
.hub-name{font-family:"IBM Plex Sans",sans-serif;font-weight:600;font-size:15px;color:var(--navy);text-align:center;line-height:19px}

/* welcome */
.welcome{left:0;top:1189px;width:1200px;height:434px;background:linear-gradient(90deg,#0c3e94,#0b45a0 50%,#0c4aa8)}
.welcome-photo{left:163px;top:1248px;width:320px;height:300px;background:linear-gradient(135deg,#b7875a,#d9b98c 40%,#8a6b7a 70%,#3c2f4d);border:14px solid var(--navy)}
.welcome-kicker{left:575px;top:1233px;font-size:18px;color:#fff}
.welcome-title{left:575px;top:1254px;font-size:30px;color:#fff;letter-spacing:-.3px}
.welcome-rule{left:575px;top:1300px;width:116px;height:3px;background:#fff}
.welcome-text{left:575px;top:1340px;width:490px;font-size:16px;line-height:22.6px;color:#eaf0fb}
.welcome-btn{left:577px;top:1539px;width:110px;height:32px;line-height:32px;text-align:center;background:#fff;color:var(--blue);font-size:15px}

/* team */
.team{left:0;top:1623px;width:1200px;height:452px;background:var(--grey-bg)}
.section-title{left:0;width:1200px;text-align:center;font-size:22px}
.team-card{top:1749px;width:462px;height:276px;background:#fff}
.team-photo{left:29px;top:41px;width:166px;height:199px}
.team-name{left:222px;top:32px;font-family:"Poppins",sans-serif;font-weight:700;font-size:17px;color:var(--navy)}
.team-bio{left:223px;top:74px;width:216px;font-size:12.5px;line-height:17.6px;color:#222}
.team-btn{left:224px;top:215px;width:87px;height:25px;line-height:25px;text-align:center;background:var(--blue);color:#fff;font-size:11.5px}

/* blog */
.blog-card{top:2187px;width:299px;height:376px;border:1px solid var(--line);background:#fff}
.blog-img{left:0;top:0;width:297px;height:201px}
.blog-title{left:23px;top:228px;width:260px;font-size:14px;font-weight:500;line-height:18px;color:#111}
.blog-text{left:24px;top:276px;width:250px;font-size:12.5px;line-height:17.6px;color:#333}
.blog-link{left:25px;top:339px;font-size:13px;font-weight:600;color:var(--blue);text-decoration:underline}

/* cta */
.cta{left:0;top:2605px;width:1200px;height:135px;background:var(--blue)}
.cta-text{left:130px;top:2648px;width:480px;font-family:"Poppins",sans-serif;font-weight:700;font-size:21px;line-height:30px;color:#fff}
.cta-btn{left:934px;top:2647px;width:134px;height:48px;line-height:44px;text-align:center;border:2px solid #fff;color:#fff;font-size:14px;font-weight:600}

/* footer */
.footer{left:0;top:2740px;width:1200px;height:345px;background:var(--footer)}
.foot-logo{left:132px;top:2790px;display:flex;flex-direction:column;align-items:center;gap:18px;width:252px}
.foot-logo .logo-square{width:60px;height:60px;background:var(--blue)}
.foot-logo .logo-name{color:#fff;font-size:24px;font-weight:500;letter-spacing:1px}
.foot-head{top:2787px;font-size:13px;font-weight:600;color:#fff;letter-spacing:.5px}
.foot-menu{left:459px;top:2823px;font-size:12px;line-height:20px;list-style:none;color:var(--footer-text)}
.foot-item{display:flex;align-items:center;gap:11px;font-size:12px;line-height:15.5px;color:var(--footer-text)}
.foot-circle{width:24px;height:24px;border-radius:50%;background:#fff;display:flex;align-items:center;justify-content:center;flex:none}
.foot-rule{left:132px;top:3003px;width:936px;height:1px;background:#333}
.copyright{left:0;width:1200px;top:3044px;text-align:center;font-size:10px;color:#ccc}
</style>
</head>
<body>

<!-- Hero -->
<section class="abs hero" role="img" aria-label="Photograph of a stone and timber office building at dusk with autumn trees"></section>
<a class="abs logo" href="#"><span class="logo-square"></span><span class="logo-name">Harbor Crest Advisory</span></a>
<nav class="abs nav"><a class="active" href="#">HOME</a><a href="#">ABOUT US</a><a href="#">SERVICES</a><a href="#">OUR TEAM</a><a href="#">CONTACT US</a></nav>
<h1 class="abs heading hero-title">FINANCIAL SERVICES FIRM</h1>
<p class="abs hero-sub">Lorem Ipsum is simply dummy text of the printing and typesetting</p>
<a class="abs btn hero-btn" href="#">READ MORE</a>
<div class="abs dots"><i></i><i></i><i class="on"></i><i></i><i></i></div>

<!-- Five sides -->
<h2 class="abs heading five-title">FIVE SIDES OF WEALTH MANAGEMENT</h2>
<div class="divider" style="top:717px"><span></span><span></span></div>

<div class="abs pillar center" style="left:410px;top:760px;width:380px">
  <h3>Risk Management &amp; Asset Protection.</h3>
  <p>Lorem ipsum dolor sit amet, consectetur adipiscing elit, sed do eiusmod tempor incididunt ut labore et dolore</p>
</div>
<div class="abs pillar right" style="left:171px;top:896px;width:240px">
  <h3>Leverage &amp; Financing</h3>
  <p>Lorem ipsum dolor sit amet, consectetur adipiscing elit, sed do eiusmod tempor incididunt ut labore et dolore</p>
</div>
<div class="abs pillar" style="left:799px;top:898px;width:240px">
  <h3>Asset Management and Investing</h3>
  <p>Lorem ipsum dolor sit amet, consectetur adipiscing elit, sed do eiusmod tempor incididunt ut labore et dolore</p>
</div>
<div class="abs pillar right" style="left:127px;top:1035px;width:240px">
  <h3>Legal &amp; Business Structuring</h3>
  <p>Lorem ipsum dolor sit amet, consectetur adipiscing elit, sed do eiusmod tempor incididunt ut labore et dolore</p>
</div>
<div class="abs pillar" style="left:836px;top:1037px;width:240px">
  <h3>Tax Efficient Strategies</h3>
  <p>Lorem ipsum dolor sit amet, consectetur adipiscing elit, sed do eiusmod tempor incididunt ut labore et dolore</p>
</div>

<div class="abs icon-ring" style="left:567px;top:845px">
  <svg width="44" height="44" viewBox="0 0 44 44" fill="none" stroke="#0d1d5c" stroke-width="2"><circle cx="22" cy="17" r="5" fill="#0d1d5c"/><path d="M12 34c0-6 4-10 10-10s10 4 10 10z" fill="#0d1d5c"/><circle cx="22" cy="4" r="2"/><circle cx="6" cy="12" r="2"/><circle cx="38" cy="12" r="2"/><circle cx="4" cy="26" r="2"/><circle cx="40" cy="26" r="2"/><path d="M22 6v5M8 13l7 3M36 13l-7 3"/></svg>
</div>
<div class="abs icon-ring" style="left:438px;top:906px">
  <svg width="44" height="44" viewBox="0 0 44 44" fill="none" stroke="#0d1d5c" stroke-width="2.2"><circle cx="24" cy="13" r="9"/><path d="M27 9h-4a2 2 0 0 0 0 4h2a2 2 0 0 1 0 4h-4M24 7v2M24 17v2"/><path d="M4 30l8-5h8l4 2h6l8-5M4 38l6-4h14l12-8" stroke-linecap="round"/></svg>
</div>
<div class="abs icon-ring" style="left:699px;top:906px">
  <svg width="44" height="44" viewBox="0 0 44 44"><circle cx="22" cy="22" r="15" fill="none" stroke="#0d1d5c" stroke-width="6" stroke-dasharray="5 3.6"/><circle cx="22" cy="22" r="11" fill="#0d1d5c"/><text x="22" y="27.5" text-anchor="middle" font-family="IBM Plex Sans,sans-serif" font-weight="600" font-size="15" fill="#fff">$</text></svg>
</div>
<div class="abs icon-ring" style="left:409px;top:1035px">
  <svg width="44" height="44" viewBox="0 0 44 44"><rect x="16" y="8" width="12" height="6" rx="2" fill="none" stroke="#0d1d5c" stroke-width="2.4"/><rect x="6" y="13" width="32" height="22" rx="3" fill="#0d1d5c"/><rect x="6" y="22" width="32" height="2" fill="#fff"/><rect x="19" y="20" width="6" height="6" fill="#fff"/></svg>
</div>
<div class="abs icon-ring" style="left:726px;top:1035px">
  <svg width="44" height="44" viewBox="0 0 44 44" fill="none" stroke="#0d1d5c" stroke-width="2"><path d="M9 5h22l5 5v29H9z"/><rect x="12" y="9" width="20" height="11" fill="#0d1d5c"/><text x="22" y="18" text-anchor="middle" font-family="IBM Plex Sans,sans-serif" font-weight="600" font-size="9" fill="#fff" stroke="none">TAX</text><path d="M13 25h18M13 29h18M13 33h12"/></svg>
</div>
<div class="abs hub">
  <span class="hub-square"></span>
  <span class="hub-name">Harbor Crest<br>Advisory</span>
</div>

<!-- Welcome -->
<section class="abs welcome"></section>
<div class="abs welcome-photo" role="img" aria-label="Photograph of stacked coins on banknotes"></div>
<p class="abs welcome-kicker">WELCOME TO</p>
<h2 class="abs heading welcome-title">HARBOR CREST ADVISORY</h2>
<div class="abs welcome-rule"></div>
<p class="abs welcome-text">Sed ut perspiciatis unde omnis iste natus error sit voluptatem accusantium doloremque laudantium, totam rem aperiam, eaque ipsa quae ab illo inventore veritatis et quasi architecto beatae vitae dicta sunt explicabo. Nemo enim ipsam voluptatem quia voluptas sit aspernatur aut odit aut fugit, sed quia consequuntur magni dolores eos qui ratione voluptatem sequi nesciunt. Neque porro quisquam est, qui dolorem ipsum quia dolor sit amet</p>
<a class="abs btn welcome-btn" href="#">READ MORE</a>

<!-- Team -->
<section class="abs team"></section>
<h2 class="abs heading section-title" style="top:1660px">OUR TEAM</h2>
<div class="divider" style="top:1703px"><span></span><span></span></div>

<article class="abs team-card" style="left:129px">
  <div class="abs team-photo" role="img" aria-label="Portrait photo of Marcus Ellery" style="background:linear-gradient(160deg,#5f8a4a,#2f4a2e 60%,#2a2d3a)"></div>
  <h3 class="abs team-name">Marcus Ellery</h3>
  <p class="abs team-bio">Marcus Ellery is the Financial Strategist and Founder who partners with C-Suite Executives, Family Offices, Real Estate Investors and Closely Held Business Owners to protect and maximize their wealth.</p>
  <a class="abs btn team-btn" href="#">READ MORE</a>
</article>
<article class="abs team-card" style="left:606px">
  <div class="abs team-photo" role="img" aria-label="Portrait photo of Graham Holloway" style="background:linear-gradient(160deg,#6b5a4c,#4a3e36 50%,#4b3fb8)"></div>
  <h3 class="abs team-name">Graham Holloway</h3>
  <p class="abs team-bio">Graham Holloway is the CFO and Strategist for our closely held businesses. As a former CPA, he takes in-depth roles in closely held companies as a financial consultant during times of exit or transition.</p>
  <a class="abs btn team-btn" href="#">READ MORE</a>
</article>

<!-- Blog -->
<h2 class="abs heading section-title" style="top:2108px">LATEST BLOG</h2>
<div class="divider" style="top:2151px"><span></span><span></span></div>

<article class="abs blog-card" style="left:132px">
  <div class="abs blog-img" role="img" aria-label="Photograph of an old bank vault door" style="background:linear-gradient(135deg,#3a4a5c,#6a5a3a 50%,#2a2a2a)"></div>
  <h3 class="abs blog-title">LOREM IPSUM DOLOR SIT AMET CONSECTETU</h3>
  <p class="abs blog-text">Lorem ipsum dolor sit amet, consec tetur adipiscing elit, sed do eiusmod tempor incididunt ut labore.</p>
  <a class="abs blog-link" href="#">READ MORE</a>
</article>
<article class="abs blog-card" style="left:450px">
  <div class="abs blog-img" role="img" aria-label="Photograph of the office building on a sunny day" style="background:linear-gradient(180deg,#3d7fd0,#8fb4dc 35%,#6a6058 65%,#7f7c74)"></div>
  <h3 class="abs blog-title">LOREM IPSUM DOLOR SIT AMET CONSECTETU</h3>
  <p class="abs blog-text">Lorem ipsum dolor sit amet, consec tetur adipiscing elit, sed do eiusmod tempor incididunt ut labore.</p>
  <a class="abs blog-link" href="#">READ MORE</a>
</article>
<article class="abs blog-card" style="left:769px">
  <div class="abs blog-img" role="img" aria-label="Photograph of an advisor reviewing charts at a desk" style="background:linear-gradient(135deg,#e9e2d8,#f4efe8 45%,#4a4038)"></div>
  <h3 class="abs blog-title">LOREM IPSUM DOLOR SIT AMET CONSECTETU</h3>
  <p class="abs blog-text">Lorem ipsum dolor sit amet, consec tetur adipiscing elit, sed do eiusmod tempor incididunt ut labore.</p>
  <a class="abs blog-link" href="#">READ MORE</a>
</article>

<!-- Call to action -->
<section class="abs cta"></section>
<p class="abs cta-text">Lorem ipsum dolor sit amet consectetur adipiscing elit sed do eiusmod.</p>
<a class="abs btn cta-btn" href="#">CONTACT US</a>

<!-- Footer -->
<footer class="abs footer"></footer>
<div class="abs foot-logo"><span class="logo-square"></span><span class="logo-name">Harbor Crest Advisory</span></div>

<h4 class="abs foot-head" style="left:459px">MENU</h4>
<ul class="abs foot-menu"><li>HOME</li><li>ABOUT US</li><li>SERVICES</li><li>OUR TEAM</li><li>CONTACT US</li></ul>

<h4 class="abs foot-head" style="left:663px">CONTACT US</h4>
<div class="abs foot-item" style="left:661px;top:2827px">
  <span class="foot-circle"><svg width="12" height="14" viewBox="0 0 12 14"><path d="M6 0a5 5 0 0 0-5 5c0 4 5 9 5 9s5-5 5-9a5 5 0 0 0-5-5z" fill="#1b1b1b"/><circle cx="6" cy="5" r="2" fill="#fff"/></svg></span>
  <span>5120 Birchmont Road<br>Alder Bay, WA 98112</span>
</div>
<div class="abs foot-item" style="left:661px;top:2878px">
  <span class="foot-circle"><svg width="12" height="12" viewBox="0 0 12 12"><path d="M2.5 0.5l2 2.5-1.2 1.4a7 7 0 0 0 4.3 4.3L9 7.5l2.5 2-1 1.8C6 11.5.5 6 .7 1.5z" fill="#1b1b1b"/></svg></span>
  <span>Call Us<br>555.014.2270</span>
</div>
<div class="abs foot-item" style="left:661px;top:2929px">
  <span class="foot-circle"><svg width="12" height="9" viewBox="0 0 12 9"><rect width="12" height="9" rx="1" fill="#1b1b1b"/><path d="M0.5 0.8L6 5l5.5-4.2" fill="none" stroke="#fff" stroke-width="1"/></svg></span>
  <span>E mail Us<br>info@HarborCrestAdvisory.com</span>
</div>

<h4 class="abs foot-head" style="left:963px">FOLLOW US</h4>
<div class="abs foot-item" style="left:962px;top:2827px"><span class="foot-circle"></span><span>Like us on<br>CHATTERLY</span></div>
<div class="abs foot-item" style="left:962px;top:2878px"><span class="foot-circle"></span><span>Follow us on<br>PINGLINE</span></div>
<div class="abs foot-item" style="left:962px;top:2929px"><span class="foot-circle"></span><span>Follow us on<br>LINKWELL</span></div>

<div class="abs foot-rule"></div>
<p class="abs copyright">Copyright © 2021 All Rights Reserved</p>

</body>
</html>
```